American cannabis tech company business card design

Thrum.com is seeking a modern, professional, and brand-aligned business card that represents our company and its core values: Mission, Story, Values, and Impact. As an innovative cannabis company, we want a business card that is not only visually appealing but also serves as a representation of who we are and what we stand for.

Project Scope: Design a double-sided business card that integrates our brand identity and core values. Incorporate our key brand elements, ensuring a sleek and contemporary aesthetic. Visually reflect our core values (Mission, Story, Values, Impact) in a way that is engaging yet professional.

Target Market(s)

Vendors, third parties,

Contact Information for Business Card

Contact details (name, title, email, phone, website, etc.)

Font styles to use
Other font styles liked:
• Caslon, Centra

Colors

Designer to choose colors to be used in the design.

Requirements
Must have
• Thrum.com logo and branding A creative yet clean way to integrate our core values (Mission, Story, Values, Impact) Modern typography and a well-structured layout
Nice to have
• forest green, grey, white, black
Should not have
• references to marijuana, leafs, plants, or related product

```html
<!DOCTYPE html>
<html lang="en">
<head>
<meta charset="UTF-8">
<title>Thrum.com Business Card</title>
<link rel="stylesheet" href="https://fonts.googleapis.com/css2?family=Montserrat:wght@400;700;800&display=swap">
<style>
  :root {
    --forest: #1b331c;
    --ink: #2b2b2b;
    --card: #ffffff;
    --backdrop: #3c3c3c;
    --radius: 26px;
  }
  * { margin: 0; padding: 0; box-sizing: border-box; }
  html, body {
    width: 1200px;
    height: 689px;
    overflow: hidden;
    background: var(--backdrop);
    font-family: "Montserrat", sans-serif;
  }
  .stage {
    width: 1200px;
    height: 689px;
    display: flex;
    align-items: center;
    justify-content: center;
    gap: 48px;
  }
  .card {
    width: 520px;
    height: 297px;
    background: var(--card);
    border-radius: var(--radius);
    position: relative;
  }
  .card--front {
    display: flex;
    align-items: center;
    justify-content: center;
  }
  .brand-name {
    font-weight: 800;
    font-size: 96px;
    letter-spacing: 2px;
    color: var(--forest);
    line-height: 1;
  }
  .card--back {
    display: flex;
    align-items: center;
    justify-content: center;
    gap: 22px;
    padding-top: 10px;
  }
  .holder {
    text-align: right;
  }
  .holder__name {
    font-weight: 700;
    font-size: 24px;
    letter-spacing: 0.5px;
    color: var(--forest);
  }
  .holder__title {
    font-weight: 400;
    font-size: 14px;
    color: var(--ink);
    margin-top: 2px;
  }
  .divider {
    width: 1.5px;
    height: 84px;
    background: var(--forest);
  }
  .contacts {
    list-style: none;
    display: flex;
    flex-direction: column;
    gap: 6px;
  }
  .contacts__item {
    display: flex;
    align-items: center;
    gap: 8px;
    font-size: 14px;
    color: var(--ink);
  }
  .contacts__icon {
    width: 12px;
    height: 12px;
    fill: var(--forest);
    flex: none;
  }
</style>
</head>
<body>
<main class="stage">
  <section class="card card--front" aria-label="Card front">
    <span class="brand-name">THRUM</span>
  </section>

  <section class="card card--back" aria-label="Card back">
    <div class="holder">
      <p class="holder__name">OWEN HARLOW</p>
      <p class="holder__title">Managing Director</p>
    </div>
    <span class="divider"></span>
    <ul class="contacts">
      <li class="contacts__item">
        <svg class="contacts__icon" viewBox="0 0 12 12" aria-hidden="true"><path d="M1 4c0-2 2-3 5-3s5 1 5 3v1H8V4H4v1H1z M3 6h6l1 5H2z"/></svg>
        +1 555-014-7026
      </li>
      <li class="contacts__item">
        <svg class="contacts__icon" viewBox="0 0 12 12" aria-hidden="true"><path d="M1 3h10v1L6 7 1 4z M1 5l5 3 5-3v4H1z"/></svg>
        team@thrum.com
      </li>
      <li class="contacts__item">
        <svg class="contacts__icon" viewBox="0 0 12 12" aria-hidden="true"><circle cx="6" cy="6" r="5"/></svg>
        www.thrum.com
      </li>
    </ul>
  </section>
</main>
</body>
</html>
```